Graphic design for a book cover

I am a 43-year old gay man that wrote a recovery book about getting clean & sober from crystal meth addiction. The book opens with my biography and life leading up to my drug addiction and decision to get sober. It then details the 90 meetings I attended in my first 90 days of recovery, reflecting on my experiences of what I learned and how it related to my own personal story. 90 meeting in 90 days is a very typical strategy that you hear over and over as a way of building the foundation for your recovery. The book includes many stories of desperation, despair and psychosis and is intended as a learning experience for those that have not been exposed to drug addiction. It is also intended to be an inspirational message of hope for those who are struggling to stay clean.

My story is somewhat unique in that I did not start using drugs until later in life. I had a normal childhood, was in a stable 14-year relationship, earned a master degree in Psychology and a doctorate degree in Education, and held a 13-year career position as an executive VP at a college. My life took a significant turn when my relationship came to a sudden end and I was accidentally introduced to Crystal Meth as a coping mechanism at the ripe old age of 38. I went from a successful, thriving life to homeless on the streets of New York and Los Angeles within 3 1/2 years. I was arrested twice, lost contact with family, had many dark moments in an endless shit show, lived on food stamps & disability, and almost died from an overdose. I had almost given up hope.

This year I fought hard to make my way back to being a contributing member of society again, and now want to share my experience with others in hopes that it can help a larger audience. I have found that being honest and open about my journey has helped fellow addicts, and for that I want to break my personal anonymity in a public forum and speak my truth. This disease is killing people everyday, and that is due in part to the shame and guilt that has been placed on those that have fallen into using. As evidenced in my story, addiction does not discriminate and can happen to anyone. I want to take on the taboo stigma of addiction head-on and give a voice to those struggling to survive each day. The tentative title of my book is 'Lanterns After Midnight.'

The book will be used as a vehicle to drive traffic to a website where I will continue the blogs beyond 90 days and walk through my first year of recovery. I would like to see illustrations that show a transformation from dark into light. Examples can be serious, comedic or sassy, recovery-based, or interpretative. The content of the book gives some graphic examples of the darker, chaotic sides of Crystal Meth addiction. The intent is to have the cover stand out from other recovery books that have already been published in a serious but tongue-in-cheek way. This is not a new-agey approach with rainbows and waterfalls. This book gets gritty and it's okay to convey a raw and naked account of what one goes through in addiction and then recovery.

Logo Text

"Lanterns After Midnight" is the title of the book and we'll need a subtitle of no more than 20 words that we can change if needed. An example could be "A gay man's descent into the hell of crystal meth addiction and how he's fighting his way back." By Derek Halvorsen

```html
<!DOCTYPE html>
<html lang="en">
<head>
<meta charset="utf-8">
<title>Lanterns After Midnight — Book Cover</title>
<link rel="stylesheet" href="https://fonts.googleapis.com/css2?family=Londrina+Solid:wght@400&family=Roboto:wght@400&family=Great+Vibes&family=Montserrat:wght@400;700&display=swap">
<style>
  :root {
    --page-bg: #f2f2f2;
    --cover-dark: #050505;
    --cover-mid: #2a2a2a;
    --ink-light: #ffffff;
    --ink-soft: #d6d6d6;
    --ink-muted: #8a8a8a;
    --glow-core: #f6f8f7;
    --glow-mid: #b9c0be;
    --rock: #2b2723;
    --rock-dark: #12100e;
  }
  html, body {
    margin: 0;
    padding: 0;
    width: 1200px;
    height: 800px;
    overflow: hidden;
    background: var(--page-bg);
  }
  .canvas {
    position: relative;
    width: 1200px;
    height: 800px;
  }
  .cover {
    position: absolute;
    top: 115px;
    width: 380px;
    height: 570px;
    overflow: hidden;
    box-shadow: 0 10px 30px rgba(0,0,0,0.18);
  }

  /* Back cover */
  .back-cover {
    left: 150px;
    background: linear-gradient(160deg, #2e2e2e 0%, #1c1c1c 40%, #111 100%);
    font-family: "Montserrat", Arial, sans-serif;
    color: var(--ink-soft);
  }
  .back-body {
    position: absolute;
    left: 38px;
    top: 118px;
    width: 304px;
  }
  .back-text {
    margin: 0 0 16px;
    font-size: 8.6px;
    line-height: 1.55;
  }
  .back-heading {
    margin: 4px 0 16px;
    font-size: 10px;
    font-weight: 700;
    letter-spacing: 0.6px;
    text-align: center;
    color: var(--ink-light);
  }
  .back-cta {
    margin: 22px 0 10px;
    font-size: 8.6px;
    font-weight: 700;
    line-height: 1.4;
    text-align: center;
    letter-spacing: 0.4px;
    color: var(--ink-light);
  }
  .back-site {
    margin: 0;
    font-size: 8px;
    letter-spacing: 0.8px;
    text-align: center;
    color: var(--ink-muted);
  }

  /* Front cover */
  .front-cover {
    left: 570px;
    background: linear-gradient(160deg, var(--cover-mid) 0%, #141414 35%, var(--cover-dark) 70%);
  }
  .cover-title {
    position: absolute;
    left: 30px;
    top: 42px;
    margin: 0;
    font-family: "Londrina Solid", "Arial Narrow", sans-serif;
    font-weight: 400;
    font-size: 52px;
    line-height: 1.02;
    color: var(--ink-light);
    letter-spacing: 0.5px;
  }
  .cover-title span { display: block; }
  .tunnel-scene {
    position: absolute;
    left: 0;
    top: 250px;
    width: 380px;
    height: 320px;
    background:
      radial-gradient(ellipse 54px 68px at 56% 42%, var(--glow-core) 0%, #e7ebea 60%, var(--glow-mid) 85%, transparent 100%),
      radial-gradient(ellipse 100px 115px at 56% 46%, var(--rock) 0%, #1d1a17 55%, transparent 100%),
      radial-gradient(ellipse 190px 110px at 56% 78%, var(--rock-dark) 0%, transparent 100%);
  }
  .cover-subtitle {
    position: absolute;
    left: 24px;
    top: 420px;
    width: 336px;
    margin: 0;
    font-family: "Roboto", Arial, sans-serif;
    font-size: 13.5px;
    line-height: 1.25;
    color: var(--ink-light);
  }
  .cover-author {
    position: absolute;
    left: 0;
    width: 380px;
    top: 468px;
    margin: 0;
    text-align: center;
    font-family: "Great Vibes", cursive;
    font-size: 26px;
    color: var(--ink-light);
  }
</style>
</head>
<body>
  <main class="canvas">
    <section class="cover back-cover">
      <div class="back-body">
        <p class="back-text">Lorem ipsum dolor sit amet, consectetuer adipiscing elit. Maecenas porttitor congue massa. Fusce posuere, magna sed pulvinar ultricies, purus lectus malesuada libero, sit amet commodo magna eros quis urna. Nunc viverra imperdiet enim.</p>
        <p class="back-text">Donec nonummy, enim in lacinia pulvinar, velit tellus scelerisque augue, ac posuere libero urna eget neque. Cras ipsum. Vestibulum pretium, lectus nec venenatis volutpat, purus lectus ultrices risus, a condimentum risus mi et quam.</p>
        <p class="back-text">Fusce auctor, metus eu ultricies vulputate, sapien nibh faucibus ligula, eget sollicitudin augue risus et dolor. Aenean pellentesque, tortor in cursus mattis, mauris diam malesuada ligula, ac vestibulum neque turpis ut enim.</p>
        <p class="back-heading">PLACE YOUR 6 X 9 COVER TEXT HERE</p>
        <p class="back-text">Lorem ipsum dolor sit amet, consectetuer adipiscing elit. Sed erat. In in velit quis arcu ornare laoreet. Curabitur adipiscing luctus massa. Integer ut purus ac augue commodo commodo.</p>
        <p class="back-cta">VISIT THE AUTHORS<br>WEBSITE AT:</p>
        <p class="back-site">WWW.LANTERNSAFTERMIDNIGHT.COM</p>
      </div>
    </section>

    <section class="cover front-cover">
      <h1 class="cover-title">
        <span>Lanterns</span>
        <span>After</span>
        <span>Midnight</span>
      </h1>
      <div class="tunnel-scene" role="img" aria-label="Photograph of a lone figure standing at the bright mouth of a dark rock tunnel"></div>
      <p class="cover-subtitle">A gay man's descent into the hell of crystal meth addiction and how he's fighting his way back.</p>
      <p class="cover-author">Derek Halvorsen</p>
    </section>
  </main>
</body>
</html>
```